Field Notes for Business Risk Advisors

I am writing a best practice book for commercial lines insurance brokers. The subtitle is Nobody Promised The Trail Was Flat. So I want a graphic of maybe someone hiking the summit. I posted an example but don't feel limited I just foudn something I liked.

This is a business book

I just mocked up an example. I dont want designers limited by my design. I am looking for juggling to be artistically displayed on the front cover. I incorporated my name into the logo but probably dont want that in my final design. Should just have my name and designations Marek Dallow, AAi, CWCP

Commercial Insurance Agents

Insurance

Sans Serif

• Must have the title of the book
Field Notes
for Business Risk
Advisors

Also the sub title Nobody Promised The Trail Was Flat

My Name on front cover Marek Dallow, AAI, CWCP

Book Cover should be black. I uploaded a copy of my work comp playbook for my desired color scehme.

My Lantern Logo on front cover and Tidewell logo on back cover
• Color should be black gray adn red using color from my logo.

```html
<!DOCTYPE html>
<html lang="en">
<head>
<meta charset="utf-8">
<title>Field Notes for Business Risk Advisors – Cover</title>
<link rel="stylesheet" href="https://fonts.googleapis.com/css2?family=Questrial&family=Open+Sans:wght@400&display=swap">
<style>
  :root {
    --red: #e0261b;
    --white: #ffffff;
    --black: #000000;
    --front-bottom: #5b5b66;
    --back-top: #1e1e20;
    --back-bottom: #56575c;
    --page: #ffffff;
    --body-text: #f2f2f2;
    --art-core: #9a9a9a;
  }
  * { box-sizing: border-box; margin: 0; padding: 0; }
  html, body { width: 789px; height: 1200px; overflow: hidden; background: var(--page); }
  .canvas { position: relative; width: 789px; height: 1200px; }

  .cover {
    position: absolute;
    width: 335px;
    height: 473px;
    overflow: hidden;
    transform-origin: top left;
  }
  .cover--small { transform: scale(0.863); }

  /* Front */
  .cover-front { background: linear-gradient(180deg, var(--black) 0%, #0c0b14 35%, var(--front-bottom) 100%); }
  .title {
    position: absolute; top: 10px; left: 0; width: 100%;
    text-align: center; font-family: "Questrial", sans-serif; line-height: 1.02;
  }
  .title__lead { display: block; color: var(--red); font-size: 29px; }
  .title__mid { display: block; color: var(--white); font-size: 31px; margin-top: 2px; }
  .title__end { display: block; color: var(--white); font-size: 35px; margin-top: 2px; }
  .subtitle {
    position: absolute; top: 113px; left: 0; width: 100%;
    text-align: center; color: var(--white);
    font-family: "Questrial", sans-serif; font-size: 14px;
  }
  .cover-art { position: absolute; left: 34px; top: 149px; width: 268px; height: 268px; }
  .brand-mark {
    position: absolute; top: 416px; left: 0; width: 100%;
    text-align: center; color: var(--white);
    font-family: "Questrial", sans-serif; font-size: 17px; letter-spacing: 4px;
  }
  .author {
    position: absolute; top: 449px; left: 0; width: 100%;
    text-align: center; color: var(--white);
    font-family: "Questrial", sans-serif; font-size: 10.5px;
  }

  /* Back */
  .cover-back { background: linear-gradient(180deg, var(--back-top) 0%, var(--back-bottom) 100%); }
  .back-heading {
    position: absolute; top: 48px; left: 0; width: 100%;
    text-align: center; color: var(--red);
    font-family: "Questrial", sans-serif; font-size: 29px;
  }
  .back-rule {
    position: absolute; top: 94px; left: 55px; width: 225px; height: 1.5px;
    background: linear-gradient(90deg, transparent, var(--red) 30%, var(--red) 70%, transparent);
  }
  .back-copy {
    position: absolute; top: 113px; left: 22px; width: 291px;
    text-align: center; color: var(--body-text);
    font-family: "Open Sans", sans-serif; font-size: 9.6px; line-height: 13.8px;
  }
  .back-copy p + p { margin-top: 14px; }
  .publisher-mark {
    position: absolute; top: 370px; left: 0; width: 100%;
    text-align: center; color: var(--white);
    font-family: "Questrial", sans-serif; font-size: 24px;
  }
</style>
</head>
<body>
<div class="canvas">

  <!-- Front cover, large -->
  <section class="cover cover-front" style="left:45px; top:75px;">
    <h1 class="title">
      <span class="title__lead">Field Notes</span>
      <span class="title__mid">for Business Risk</span>
      <span class="title__end">Advisors</span>
    </h1>
    <p class="subtitle">Nobody Promised The Trail Was Flat</p>
    <svg class="cover-art" viewBox="0 0 268 268" role="img" aria-label="Cover illustration: red emblem framing a greyscale photo of a model house, pen, coins and calculator">
      <defs>
        <radialGradient id="art-a" cx="50%" cy="50%" r="50%">
          <stop offset="0%" stop-color="#a8a8a8"/>
          <stop offset="68%" stop-color="#6e6e6e"/>
          <stop offset="74%" stop-color="#c0261b"/>
          <stop offset="100%" stop-color="#6a2a22" stop-opacity="0.6"/>
        </radialGradient>
      </defs>
      <circle cx="134" cy="134" r="134" fill="url(#art-a)"/>
    </svg>
    <div class="brand-mark">LANTERN</div>
    <p class="author">Marek Dallow, AAI, CWCP</p>
  </section>

  <!-- Back cover, large -->
  <section class="cover cover-back" style="left:413px; top:75px;">
    <h2 class="back-heading">Trust The Process</h2>
    <div class="back-rule"></div>
    <div class="back-copy">
      <p>Field Notes is the culmination of 36 years of experience as a commercial line's producer.</p>
      <p>The proven strategy discussed in this book will change your trajectory as a broker. It will teach you how to attract and retain good risk management accounts and grow your book of business. Marek's other guide, The Work Comp Field Guide for Employers has sold over 3,000 copies making it a leading seller on risk management.</p>
      <p>Marek is passionate about risk management. He is a partner at Harlow, Fenwick and Ames and has administered the Regional Certified Workers' Compensation Professional Program (CWCP) since its inception in 1999. Marek graduated with a Risk Management degree from Redmont State University and is married with two sons.</p>
    </div>
    <div class="publisher-mark">Tidewell</div>
  </section>

  <!-- Back cover, small -->
  <section class="cover cover-back cover--small" style="left:63px; top:713px;">
    <h2 class="back-heading">Trust The Process</h2>
    <div class="back-rule"></div>
    <div class="back-copy">
      <p>Field Notes is the culmination of 36 years of experience as a commercial line's producer.</p>
      <p>The proven strategy discussed in this book will change your trajectory as a broker. It will teach you how to attract and retain good risk management accounts and grow your book of business. Marek's other guide, The Work Comp Field Guide for Employers has sold over 3,000 copies making it a leading seller on risk management.</p>
      <p>Marek is passionate about risk management. He is a partner at Harlow, Fenwick and Ames and has administered the Regional Certified Workers' Compensation Professional Program (CWCP) since its inception in 1999. Marek graduated with a Risk Management degree from Redmont State University and is married with two sons.</p>
    </div>
    <div class="publisher-mark">Tidewell</div>
  </section>

  <!-- Front cover, small -->
  <section class="cover cover-front cover--small" style="left:433px; top:713px;">
    <h1 class="title">
      <span class="title__lead">Field Notes</span>
      <span class="title__mid">for Business Risk</span>
      <span class="title__end">Advisors</span>
    </h1>
    <p class="subtitle">Nobody Promised The Trail Was Flat</p>
    <svg class="cover-art" viewBox="0 0 268 268" role="img" aria-label="Cover illustration: red emblem framing a greyscale photo of a model house, pen, coins and calculator">
      <defs>
        <radialGradient id="art-b" cx="50%" cy="50%" r="50%">
          <stop offset="0%" stop-color="#a8a8a8"/>
          <stop offset="68%" stop-color="#6e6e6e"/>
          <stop offset="74%" stop-color="#c0261b"/>
          <stop offset="100%" stop-color="#6a2a22" stop-opacity="0.6"/>
        </radialGradient>
      </defs>
      <circle cx="134" cy="134" r="134" fill="url(#art-b)"/>
    </svg>
    <div class="brand-mark">LANTERN</div>
    <p class="author">Marek Dallow, AAI, CWCP</p>
  </section>

</div>
</body>
</html>
```